Forex website redesign

We need an attractive good looking website design that increase the apatite of our visitors to subscribe to our advisory service, beside the fact that we do offer very high quality service.

Our service is where we connect to investor accounts who are subscribed, to automatically deliver and execute our advise to buy or sell straight onto their account using high tech software.

The final design should communicate financial safty and growth.
Updates

Here is something to keep in mind about our business model that may help you in your design, we SHOW people the right way to invest, so they can make money instead of going somewere else and lose it. Beside that point, most websites in forex that includes pictures of happy and excited people who make money ALWAY turn out to be scam. So please try not to position our business that way in visitor first impression once he/she visit our site.

Thank you for your help :)

Target Market(s)

Financial Market, 20-70 years old

Industry/Entity Type

Financial

Requirements
Must have
• Call to action feature + Logo redesign. Please visit www.velmoratrade.com to get an idea of how we want it. Also include the personal photos of our advisors in your deign.

```html
<!DOCTYPE html>
<html lang="en">
<head>
<meta charset="utf-8">
<title>Velmora FX LTD</title>
<link href="https://fonts.googleapis.com/css2?family=Open+Sans:ital,wght@0,300;0,400;0,600;0,700;1,400&display=swap" rel="stylesheet">
<style>
:root{
  --ink:#2d2d2d;
  --muted:#6b6b6b;
  --navy:#1f3147;
  --slate:#4e6378;
  --band:#6a7f94;
  --gold:#fbb800;
  --orange:#f39c12;
  --blue-head:#2f4f78;
  --soft:#f6f6f6;
  --line:#d8d8d8;
  --white:#ffffff;
}
*{margin:0;padding:0;box-sizing:border-box}
html,body{width:762px;height:1200px;overflow:hidden;background:var(--white)}
body{position:relative;font-family:"Open Sans",Arial,sans-serif;color:var(--ink)}
.abs{position:absolute}

/* header */
.brand{left:51px;top:20px;display:flex;align-items:center;gap:8px}
.brand-mark{width:22px;height:22px;background:var(--slate);border-radius:50%}
.brand-name{font-size:19px;font-weight:700;color:var(--slate);line-height:1}
.brand-tag{left:81px;top:44px;font-size:8.5px;font-weight:700;color:var(--navy)}
.nav{left:305px;top:40px;display:flex;font-size:11.5px;color:#555}
.nav span{padding:0 8px;border-left:1px solid #bbb;line-height:13px}
.nav span:first-child{border-left:none}

/* hero */
.hero-band{left:0;top:73px;width:762px;height:281px;background:linear-gradient(#7b8fa3,#5e7388)}
.hero-panel{left:51px;top:84px;width:660px;height:270px}
.hero-title{left:0;top:120px;width:762px;text-align:center;color:var(--white);font-size:26px;font-weight:600}
.hero-sub{left:0;top:154px;width:762px;text-align:center;color:#e4e9ef;font-size:10.5px}
.video-frame{left:237px;top:183px;width:289px;height:189px;background:var(--white);box-shadow:0 1px 4px rgba(0,0,0,.3)}
.video-media{left:6px;top:5px;width:277px;height:178px;background:linear-gradient(135deg,#d6d3cc,#8d8a86 55%,#3a3b40)}
.play{width:28px;height:28px;border-radius:50%;background:rgba(20,20,20,.8);border:2px solid #fff}
.play::after{content:"";position:absolute;left:9px;top:6px;border-left:9px solid #fff;border-top:6px solid transparent;border-bottom:6px solid transparent}
.slider-arrows{left:675px;top:327px}

/* intro */
.intro-title{left:0;top:395px;width:762px;text-align:center;font-size:24px;font-weight:300;color:#333}
.intro-text{left:100px;top:427px;width:562px;text-align:center;font-size:9.5px;font-weight:300;line-height:16px;color:var(--muted)}
.feature{width:190px;height:97px;top:481px}
.feature svg{position:absolute;left:0;top:0}
.feature-title{position:absolute;top:13px;width:100%;text-align:center;color:#fff;font-size:18px;font-weight:400}
.feature-text{position:absolute;top:38px;left:12px;right:12px;text-align:center;color:#fff4cf;font-size:8px;line-height:12px}

/* signals */
.signals-band{left:0;top:611px;width:762px;height:267px;background:var(--soft)}
.signals-inner{left:18px;top:611px;width:744px;height:243px;background:var(--white)}
.signals-photo-frame{left:51px;top:647px;width:224px;height:162px;background:#fff;box-shadow:0 0 3px rgba(0,0,0,.15)}
.signals-photo{left:6px;top:5px;width:212px;height:152px;background:linear-gradient(160deg,#e3ddd3,#b8b2a9 50%,#262a33)}
.signals-title{left:294px;top:644px;font-size:23px;font-weight:300;color:#333}
.signals-text{left:294px;top:681px;width:410px;font-size:8.4px;font-weight:300;line-height:15.5px;color:#555}
.signals-text p+p{margin-top:6px}
.btn{left:294px;top:818px;width:73px;height:25px;background:linear-gradient(#51657b,#2f4157);color:#fff;font-size:9.5px;text-align:center;line-height:25px;border-radius:2px}

/* lower */
.col-title{top:919px;font-size:17px;font-weight:300;color:var(--blue-head)}
.col-title.partners{color:var(--orange)}
.quote{left:52px;top:948px;width:210px;font-size:9px;font-style:italic;line-height:16px;color:#555}
.quote-author{left:52px;top:1032px;font-size:8.5px;color:#333}
.posts{left:294px;top:947px;width:212px}
.post{border-bottom:1px solid var(--line);padding:0 0 5px;margin-bottom:8px}
.post:last-child{border-bottom:none}
.post-title{font-size:8.8px;color:#333;line-height:14px}
.post-text{font-size:8.3px;font-weight:300;color:#777;line-height:14px}
.badges{left:538px;top:955px;width:175px;display:grid;grid-template-columns:repeat(4,1fr);row-gap:14px;column-gap:6px}
.badge{height:20px;background:#c7c7c7;border-radius:3px}
.badge.round{border-radius:10px}

/* footer */
.footer{left:0;top:1106px;width:762px;height:94px;background:linear-gradient(#5c6b7e,#1e2937)}
.footer-nav{left:54px;top:1129px;font-size:9.5px;color:#fff}
.footer-nav span{padding:0 4px;border-left:1px solid #ccc}
.footer-nav span:first-child{padding-left:0;border-left:none}
.copyright{left:54px;top:1150px;font-size:7.5px;color:#cfd6df}
.social{top:1127px;width:19px;height:19px;border-radius:50%;background:#e9ecef}
</style>
</head>
<body>

<header>
  <div class="abs brand"><span class="brand-mark"></span><span class="brand-name">Velmora FX LTD</span></div>
  <div class="abs brand-tag">From Traders to Traders, THE REAL DEAL</div>
  <nav class="abs nav"><span>Home</span><span>About Us</span><span>Order</span><span>Peformance</span><span>Special</span><span>Why Us?</span><span>Contact</span></nav>
</header>

<section>
  <div class="abs hero-band"></div>
  <svg class="abs hero-panel" width="660" height="270" viewBox="0 0 660 270">
    <defs><linearGradient id="panelGrad" x1="0" y1="0" x2="0" y2="1"><stop offset="0" stop-color="#53677c"/><stop offset="1" stop-color="#1e3046"/></linearGradient></defs>
    <path d="M0 25 Q330 -20 660 25 L660 270 L0 270 Z" fill="url(#panelGrad)"/>
  </svg>
  <h1 class="abs hero-title">Velmora FX Safe Player</h1>
  <p class="abs hero-sub">Mauris vel lacus vitae felis vestibulum volutpat Etiam est nunc venenatis in tristique</p>
  <div class="abs video-frame">
    <div class="abs video-media" role="img" aria-label="Video still of an advisor in a suit seated beside a trading chart monitor"></div>
    <div class="abs play" style="left:130px;top:76px"></div>
  </div>
  <svg class="abs slider-arrows" width="24" height="20" viewBox="0 0 24 20"><path d="M8 3 L2 10 L8 17 M16 3 L22 10 L16 17" stroke="#fff" stroke-width="1.6" fill="none"/></svg>
</section>

<section>
  <h2 class="abs intro-title">Donec iaculis diam a nisi accumsan viverra</h2>
  <p class="abs intro-text">Velmora FX LTD is the ONLY forex signal service on this planet that provides full info about the traders involved including REAL personal photos, REAL personal details and portfolios, as well as YEARS of verified and consistent live trading performance.</p>

  <div class="abs feature" style="left:81px">
    <svg width="190" height="97" viewBox="0 0 190 97"><path d="M0 0 H190 V70 L95 97 L0 70 Z" fill="#fbb800"/></svg>
    <div class="feature-title">Performance</div>
    <div class="feature-text">Maecenas aliquet velit vel turpis. Mauris neque metus, malesuada nec</div>
  </div>
  <div class="abs feature" style="left:287px">
    <svg width="190" height="97" viewBox="0 0 190 97"><path d="M0 0 H190 V70 L95 97 L0 70 Z" fill="#fbb800"/></svg>
    <div class="feature-title">Order Now</div>
    <div class="feature-text">Maecenas aliquet velit vel turpis. Mauris neque metus, malesuada nec</div>
  </div>
  <div class="abs feature" style="left:494px">
    <svg width="190" height="97" viewBox="0 0 190 97"><path d="M0 0 H190 V70 L95 97 L0 70 Z" fill="#fbb800"/></svg>
    <div class="feature-title">Leo Marsh</div>
    <div class="feature-text">Maecenas aliquet velit vel turpis. Mauris neque metus, malesuada nec</div>
  </div>
</section>

<section>
  <div class="abs signals-band"></div>
  <div class="abs signals-inner"></div>
  <div class="abs signals-photo-frame">
    <div class="abs signals-photo" role="img" aria-label="Video still of an advisor in a dark suit standing before a monitor with charts"></div>
    <div class="abs play" style="left:100px;top:62px"></div>
  </div>
  <h2 class="abs signals-title">How Signals Work</h2>
  <div class="abs signals-text">
    <p>Once you subscribe, you will be re-directed to a secure page to download and set-up the EA copier on your VPS with all the instructions you need(We provide full support, and we can set it up for you for no additional charge. Once set-up, the software is of superior quality and copies flawlessly, and you have direct and total control over your account. Whereas your subscription will be renewed automatically by the end of the cycle you choose (Monthly/OR/4 months).</p>
    <p>Furthermore, you can adjust the risk set-up according to your own risk tolerance (We provide excellent and fast customer support to answer any question you may have). Nevertheless, you can unsubscribe anytime you want. And you keep 100% of the profits on your account regardless. And with no obligation.</p>
  </div>
  <div class="abs btn">Order Now</div>
</section>

<section>
  <h3 class="abs col-title" style="left:51px">What Our Clients Say</h3>
  <p class="abs quote">Mauris vel lacus vitae felis vestibulum volutpat. Etiam est nunc, venenatis in, tristique eu, imperdiet ac, nisl. Cum sociis natoque penatibus et magnis dis parturient montes, nascetur ridiculus mus. In iaculis facilisis massa. Etiam eu urna.Phasellus felis dolor</p>
  <div class="abs quote-author">By Author Name</div>

  <h3 class="abs col-title" style="left:294px">Recent Blog Post</h3>
  <div class="abs posts">
    <div class="post"><div class="post-title">Mauris vel lacus vitae felis</div><div class="post-text">Etiam est nunc, venenatis in, tristique eu imperdiet ac</div></div>
    <div class="post"><div class="post-title">Class aptent taciti sociosqu</div><div class="post-text">Curabitur metus ipsum, luctus eu, malesuada</div></div>
    <div class="post"><div class="post-title">Duis sed tellus et tortor</div><div class="post-text">Curabitur metus ipsum, luctus eu, malesuada</div></div>
  </div>

  <h3 class="abs col-title partners" style="left:538px">Clients &amp; Partners</h3>
  <div class="abs badges">
    <div class="badge"></div><div class="badge round"></div><div class="badge"></div><div class="badge"></div>
    <div class="badge"></div><div class="badge"></div><div class="badge round"></div><div class="badge"></div>
  </div>
</section>

<footer>
  <div class="abs footer"></div>
  <nav class="abs footer-nav"><span>Home</span><span>About Us</span><span>Order</span><span>Performance</span><span>Special</span><span>Why Us?</span><span>Contact</span></nav>
  <div class="abs copyright">© 2013 Company Name.  All right reserved.  Term of Use</div>
  <div class="abs social" style="left:627px"></div>
  <div class="abs social" style="left:648px"></div>
  <div class="abs social" style="left:669px"></div>
  <div class="abs social" style="left:690px"></div>
</footer>

</body>
</html>
```